Southbay Provisions, Seafood and Fresh Produce Website

Our organization is looking to design a simple, but eye catching website to show our services.
Our company exports West Australian FRESH fruit and vegetables, seafood and meat.
The website we are looking for would consist of:
- Landing Page
- Company info
- Directors bio
- Page that highlights our products
- Contact us page
We would like it to have a Chinese translated version as well.
Milo
Target Market(s)
Chinese Market
Industry/Entity Type
It Company
Number of Pages Required
1 page
Look and feel
Each slider illustrates characteristics of the customer's brand and the style your logo design should communicate.

```html
<!DOCTYPE html>
<html lang="en">
<head>
<meta charset="utf-8">
<title>Southbay Provisions</title>
<link rel="stylesheet" href="https://fonts.googleapis.com/css2?family=Open+Sans:wght@400;600;700&family=Oswald:wght@500&display=swap">
<style>
:root{
  --orange:#f26a38;
  --orange-light:#f7804f;
  --orange-btn:#f0541f;
  --green:#6aa525;
  --green-dark:#588d1c;
  --cream:#eeeee1;
  --wood-dark:#7a3f1f;
  --wood:#94532d;
  --wood-light:#a86a40;
  --ink:#222;
  --muted:#555;
  --footer:#2b2b2b;
  --white:#fff;
}
*{box-sizing:border-box;margin:0;padding:0}
html,body{width:706px;height:1200px;overflow:hidden}
body{position:relative;font-family:"Open Sans",Arial,sans-serif;color:var(--ink);background:var(--white)}
.abs{position:absolute}

/* header */
.site-header{position:absolute;left:0;top:0;width:706px;height:94px;background:linear-gradient(180deg,var(--orange-light),var(--orange))}
.brand{position:absolute;left:96px;top:28px;display:flex;align-items:center;gap:8px;color:var(--white);font-weight:700;font-size:15px;letter-spacing:.3px}
.brand-mark{width:22px;height:22px;background:var(--white);border-radius:50%}
.account-links{position:absolute;right:96px;top:15px;color:var(--white);font-size:7px;letter-spacing:.3px}
.account-links span{margin:0 5px}
.call-us{position:absolute;right:96px;top:38px;color:var(--white);font-family:"Oswald","Open Sans",sans-serif;font-weight:500;font-size:13px}
.search{position:absolute;left:480px;top:64px;width:130px;height:19px;background:var(--white);border:1px solid #ddd;font-size:7px;color:#999;padding:5px 6px}
.search svg{position:absolute;right:5px;top:4px}

/* nav */
.main-nav{position:absolute;left:0;top:94px;width:706px;height:31px;background:var(--green)}
.main-nav ul{list-style:none;position:absolute;left:90px;top:0;display:flex;height:31px}
.main-nav li{color:var(--white);font-size:9px;line-height:31px;text-align:center;border-right:1px solid rgba(255,255,255,.18)}
.main-nav li.active{background:var(--green-dark)}
.social{position:absolute;display:flex;gap:4px}
.social i{display:block;width:14px;height:14px;border-radius:50%;background:#cfcfcf}

/* hero */
.hero{position:absolute;left:0;top:125px;width:706px;height:222px;background:linear-gradient(135deg,#3a2a22 0%,#6c2a28 35%,#b8434a 55%,#4a3026 80%,#2a221c 100%)}
.hero-caption{position:absolute;left:0;bottom:0;width:706px;height:33px;background:rgba(0,0,0,.45);color:var(--white);font-size:11px;line-height:33px;padding-left:96px;letter-spacing:.2px}
.dots{position:absolute;right:96px;top:13px;display:flex;gap:4px}
.dots i{width:5px;height:5px;border-radius:50%;background:#bbb}
.dots i.on{background:var(--white)}

/* welcome */
.welcome{position:absolute;left:0;top:347px;width:706px;height:301px;background:var(--cream);text-align:center}
.welcome h1{font-weight:400;font-size:16px;margin-top:29px;color:var(--ink)}
.welcome p{font-size:7.4px;line-height:12.5px;color:#333;width:500px;margin:5px auto 0}
.btn{display:inline-block;background:var(--orange-btn);color:var(--white);font-size:7.5px;font-weight:600;text-align:center;border-radius:2px}
.welcome .btn{position:absolute;left:318px;top:95px;width:68px;height:21px;line-height:21px}
.categories{position:absolute;left:96px;top:141px;width:515px;height:119px;display:flex}
.category{position:relative;width:128.75px;height:119px}
.category .label{position:absolute;left:0;width:100%;height:25px;line-height:25px;color:var(--white);font-size:10px;text-align:center}
.label.bottom{bottom:0;background:var(--green)}
.label.top{top:0;background:#3a3a3a}
.label.top.orange{background:var(--orange)}

/* features */
.features{position:absolute;left:0;top:648px;width:706px;height:262px}
.features-bg{position:absolute;inset:0;background:linear-gradient(180deg,var(--wood-dark) 0%,var(--wood) 30%,var(--wood-light) 55%,var(--wood) 80%,var(--wood-dark) 100%)}
.feature{position:absolute;width:250px;height:83px;background:var(--white);display:flex}
.feature .thumb{width:92px;height:83px;flex:none}
.feature .body{padding:14px 0 0 16px}
.feature h3{font-weight:400;font-size:13px;color:var(--green);line-height:14px}
.feature h3.dark{color:var(--ink)}
.feature h3.orange{color:var(--orange-btn)}
.feature em{display:block;font-size:7.5px;color:#555;margin-top:2px}
.feature p{font-size:7px;color:#333;margin-top:1px}
.feature .more{font-size:7.5px;color:var(--orange-btn);margin-top:6px;display:block}
.feature .more.green{color:var(--green)}

/* info */
.info h2{position:absolute;top:944px;font-weight:400;font-size:12.5px;color:var(--ink)}
.bio-name{position:absolute;left:96px;top:1051px;font-size:7.5px;font-weight:700}
.bio-text{position:absolute;left:96px;top:1061px;width:160px;font-size:6.8px;line-height:9.6px;color:#333}
.info .btn{position:absolute;width:64px;height:17px;line-height:17px}
.services{position:absolute;left:282px;top:961px;width:138px;list-style:none}
.services li{height:22.8px;line-height:21px;font-size:6.8px;color:#333;border-bottom:1px solid #e3e3e3;padding-left:11px;position:relative}
.services li::before{content:"";position:absolute;left:1px;top:8px;width:4.5px;height:4.5px;border-radius:50%;background:var(--orange-btn)}
.services li.current{color:var(--orange-btn)}
.services li.current::before{background:#aaa}
.contact{position:absolute;left:443px;width:164px;font-size:7px;color:#333;padding-left:19px}
.contact svg{position:absolute;left:0;top:0}

/* footer */
.site-footer{position:absolute;left:0;top:1164px;width:706px;height:36px;background:var(--footer);color:#ddd;font-size:7px}
.site-footer .copy{position:absolute;left:96px;top:13px}
</style>
</head>
<body>

<header class="site-header">
  <div class="brand"><span class="brand-mark"></span>SOUTHBAY PROVISIONS</div>
  <div class="account-links">LOG IN<span>|</span>REGISTER</div>
  <div class="call-us">CALL US NOW:&nbsp; 123-456-7890</div>
  <div class="search">Search
    <svg width="9" height="9" viewBox="0 0 10 10"><circle cx="4" cy="4" r="3" fill="none" stroke="#888" stroke-width="1.3"/><line x1="6.3" y1="6.3" x2="9.3" y2="9.3" stroke="#888" stroke-width="1.4"/></svg>
  </div>
</header>

<nav class="main-nav">
  <ul>
    <li class="active" style="width:61px">HOME</li>
    <li style="width:79px">ABOUT US</li>
    <li style="width:84px">PRODUCTS</li>
    <li style="width:66px">NEWS</li>
    <li style="width:92px">CONTACT US</li>
  </ul>
  <div class="social" style="left:542px;top:8px"><i></i><i></i><i></i><i></i></div>
</nav>

<section class="hero" role="img" aria-label="Photo of raw marbled beef slices on a black tray on a dark wooden table">
  <div class="hero-caption">COMMITTED TO HIGH QUALITY AND EXCELLENCE
    <div class="dots"><i></i><i class="on"></i><i></i><i></i><i></i></div>
  </div>
</section>

<section class="welcome">
  <h1>Welcome to Southbay Provisions</h1>
  <p>Beciegast nveriti vitaesaert asety aset aplica boserde nsaert asety kertya aerafae kertyuraue styasnemo faserani iasera khatnasas taiadeser daesraeds. Casrolern atur aut oditaut. onsequuntur magni dolqui ratione voluptagni dolqui ra temsequi nesciunt orasario joasuaserya vytarsa numquam eius modi teincidunt, ut to high quality and excellenceore et dolore magnam.</p>
  <span class="btn">READ MORE</span>
  <div class="categories">
    <div class="category" role="img" aria-label="Photo of assorted fresh vegetables" style="background:linear-gradient(135deg,#4f7a2a,#a13a2a 45%,#6f9a35)"><div class="label bottom">VEGETABLES</div></div>
    <div class="category" role="img" aria-label="Black and white photo of raw meat cuts" style="background:linear-gradient(135deg,#6a6a6a,#bdbdbd 50%,#7a7a7a)"><div class="label top">MEAT</div></div>
    <div class="category" role="img" aria-label="Photo of a basket of fresh fruit" style="background:linear-gradient(135deg,#f4f0e8,#e0a12a 45%,#b3402a 75%,#f0eee6)"><div class="label bottom">FRUITS</div></div>
    <div class="category" role="img" aria-label="Photo of a prawn and salmon seafood plate" style="background:linear-gradient(135deg,#8a3a22,#e8e2dc 45%,#d9733e 70%,#f1ece6)"><div class="label top orange">SEA FOOD</div></div>
  </div>
</section>

<section class="features">
  <div class="features-bg" role="img" aria-label="Warm brown wooden plank texture background"></div>
  <article class="feature" style="left:96px;top:38px">
    <div class="thumb" role="img" aria-label="Illustration of a red delivery truck with parcels" style="background:linear-gradient(135deg,#f4f4f4,#d63a2e 50%,#e9e9e9)"></div>
    <div class="body"><h3>FREE SHIPPING</h3><em>Migytafsas deuauyt asares</em><p>Kictaesaert asetyertya aset aplicibrdedas.</p><span class="more">- READ MORE</span></div>
  </article>
  <article class="feature" style="left:358px;top:38px">
    <div class="thumb" role="img" aria-label="Black and white photo of an apple" style="background:radial-gradient(circle at 50% 55%,#222 0 30%,#999 60%,#eee)"></div>
    <div class="body"><h3 class="dark">FRESH QUALITY</h3><em>Migytafsas deuauyt asares</em><p>Kictaesaert asetyertya aset aplicibrdedas.</p><span class="more green">- READ MORE</span></div>
  </article>
  <article class="feature" style="left:96px;top:133px">
    <div class="thumb" role="img" aria-label="Photo of a person shopping online with a laptop" style="background:linear-gradient(135deg,#eef0e0,#d9b37a 50%,#c9d28a)"></div>
    <div class="body"><h3>ORDER ONLINE</h3><em>Migytafsas deuauyt asares</em><p>Kictaesaert asetyertya aset aplicibrdedas.</p><span class="more">- READ MORE</span></div>
  </article>
  <article class="feature" style="left:358px;top:133px">
    <div class="thumb" role="img" aria-label="Photo of hands holding a red gift box" style="background:linear-gradient(135deg,#f2eeea,#c73a3a 50%,#e6d2c4)"></div>
    <div class="body"><h3 class="orange">SPECIAL OFFER</h3><em>Migytafsas deuauyt asares</em><p>Kictaesaert asetyertya aset aplicibrdedas.</p><span class="more">- READ MORE</span></div>
  </article>
</section>

<section class="info">
  <h2 style="left:96px">Director’s Bio</h2>
  <div class="abs" role="img" aria-label="Portrait photo of the company director in a suit" style="left:96px;top:966px;width:161px;height:78px;background:linear-gradient(135deg,#8e98a2,#5d6570 50%,#c6ccd2)"></div>
  <div class="bio-name">Dr. Owen Carver</div>
  <p class="bio-text">Sed ut perspiciatis unde omnis iste n atus error sit volup tatem accusantium doloreque lauda ntium, totam rem aperiam, eaque ipsa quae ab illo inven tore eritfgh atis et quasi architecto bedsfatae vitae dicta sunt explibo. Nemo enim ipsam.</p>
  <span class="btn" style="left:96px;top:1118px">READ MORE</span>

  <h2 style="left:282px">Our Services</h2>
  <ul class="services">
    <li>SED UT PERSPICIATIS UNDE OMNIS</li>
    <li>SED UT PERSPICIATIS UNDE OMNIS</li>
    <li class="current">SED UT PERSPICIATIS UNDE OMNIS</li>
    <li>SED UT PERSPICIATIS UNDE OMNIS</li>
    <li>SED UT PERSPICIATIS UNDE OMNIS</li>
    <li>SED UT PERSPICIATIS UNDE OMNIS</li>
    <li>SED UT PERSPICIATIS UNDE OMNIS</li>
  </ul>
  <span class="btn" style="left:292px;top:1118px">READ MORE</span>

  <h2 style="left:443px">Our Location</h2>
  <div class="abs" role="img" aria-label="Street map showing the office location" style="left:443px;top:966px;width:163px;height:78px;background:linear-gradient(135deg,#e8e6df,#d9dcd3 50%,#ece6d2)"></div>
  <div class="contact" style="top:1052px;line-height:9px">
    <svg width="9" height="11" viewBox="0 0 9 11"><path d="M4.5 0.5a3.6 3.6 0 0 1 3.6 3.6c0 2.6-3.6 6.4-3.6 6.4S0.9 6.7 0.9 4.1A3.6 3.6 0 0 1 4.5 0.5z" fill="#777"/><circle cx="4.5" cy="4.1" r="1.3" fill="#fff"/></svg>
    Sed ut perspiciatis unde omnis iste<br>error sit voluptatem
  </div>
  <div class="contact" style="top:1074px;line-height:9px">
    <svg width="10" height="10" viewBox="0 0 10 10"><circle cx="5" cy="5" r="4.3" fill="none" stroke="#777"/><path d="M3.3 2.8l1 1-0.6.7c.4.8 1 1.4 1.8 1.8l.7-.6 1 1-.8.8c-1.8-.3-3.6-2.1-3.9-3.9z" fill="#777"/></svg>
    123-654-7890
  </div>
  <div class="contact" style="top:1091px;line-height:9px">
    <svg width="10" height="9" viewBox="0 0 10 9"><path d="M1 2.5C3.5.5 6.5.5 9 2.5L8 4 6.5 3.4V2.6c-1-.3-2-.3-3 0v.8L2 4z" fill="#777"/><rect x="2.3" y="4.6" width="5.4" height="3.8" rx=".6" fill="#777"/></svg>
    123-456-7890
  </div>
  <div class="abs" style="left:443px;top:1110px;width:164px;border-top:1px solid #e3e3e3"></div>
  <div class="contact" style="top:1119px;line-height:8px">
    <svg width="10" height="8" viewBox="0 0 10 8"><rect x=".5" y=".5" width="9" height="7" fill="#777"/><path d="M.8 1l4.2 3.2L9.2 1" fill="none" stroke="#fff" stroke-width=".9"/></svg>
    support@southbayprovisions.example
  </div>
</section>

<footer class="site-footer">
  <div class="copy">© 2015. <b>Southbay Provisions</b>. All rights reserved.</div>
  <div class="social" style="left:540px;top:11px"><i style="background:#666"></i><i style="background:#666"></i><i style="background:#666"></i><i style="background:#666"></i></div>
</footer>

</body>
</html>
```